Ceiling fan flyer design

We are after a double sided flyer design offering ceiling fan installations

Target Market(s)

Home owners

Requirements
Must have
• content listed

```html
<!DOCTYPE html>
<html lang="en">
<head>
<meta charset="utf-8">
<title>Ceiling Fan Installation Flyer</title>
<link href="https://fonts.googleapis.com/css2?family=Roboto+Condensed:wght@700;900&family=Exo+2:wght@500;600;700;800&display=swap" rel="stylesheet">
<style>
  :root{
    --bg:#f2f2f2;
    --red:#e30613;
    --blue:#0a6ab5;
    --navy:#23205a;
    --sky:#1e8fe0;
    --sky-light:#56b8f5;
    --yellow:#ffcc00;
    --peach:#fcd79a;
    --orange:#f26522;
    --ink:#1a1a1a;
    --quote:#1a73d0;
    --white:#ffffff;
    --photo-1:#cfc4b6;
    --photo-2:#8a5a3c;
  }
  *{box-sizing:border-box;margin:0;padding:0}
  html,body{width:1200px;height:1000px;overflow:hidden;background:var(--bg)}
  .canvas{position:relative;width:1200px;height:1000px}

  /* Front page */
  .front{position:absolute;left:104px;top:178px;width:457px;height:644px;background:var(--white);overflow:hidden;font-family:"Roboto Condensed",sans-serif}
  .front__head{height:127px;background:var(--red);color:var(--white);text-align:center;text-transform:uppercase;font-weight:900;line-height:1}
  .front__head .l1{font-size:64px;padding-top:12px;letter-spacing:1px}
  .front__head .l2{font-size:48px;padding-top:6px;letter-spacing:.5px}
  .front__photo{height:390px;background:linear-gradient(135deg,var(--photo-1) 0%,#e9e4dc 45%,var(--photo-2) 100%)}
  .front__foot{height:127px;background:var(--blue);color:var(--white);text-transform:uppercase;font-weight:900;position:relative}
  .front__foot .save{position:absolute;left:47px;top:8px;font-size:62px;line-height:1}
  .front__foot .off{position:absolute;right:46px;top:8px;font-size:62px;line-height:1}
  .front__foot .every{position:absolute;left:0;right:0;top:72px;text-align:center;font-size:34px;line-height:1}
  .front__foot .every sup{font-size:22px;vertical-align:12px}
  .price-badge{position:absolute;left:176px;top:432px;width:150px;height:150px;border-radius:50%;background:var(--red);border:5px solid var(--white);box-shadow:0 2px 6px rgba(0,0,0,.35);color:var(--white);font-weight:900;font-size:72px;display:flex;align-items:center;justify-content:center;letter-spacing:-2px}

  /* Back page */
  .back{position:absolute;left:640px;top:178px;width:457px;height:644px;background:var(--navy);overflow:hidden;font-family:"Exo 2",sans-serif}
  .back__inner{position:absolute;left:15px;top:0;right:17px;bottom:22px;background:linear-gradient(180deg,var(--sky) 0%,var(--sky-light) 60%,var(--sky) 100%)}
  .promo{position:absolute;left:15px;top:14px;width:425px;height:68px;background:var(--yellow);text-align:center;color:var(--ink)}
  .promo h2{font-size:22px;font-weight:700;padding-top:8px;letter-spacing:.3px}
  .promo p{font-size:10.5px;font-weight:500;line-height:1.3;margin-top:3px}
  .quote{position:absolute;top:90px;width:188px;height:130px;background:var(--white);border:2px solid var(--sky);border-radius:12px;color:var(--quote);padding:22px 12px 0 28px}
  .quote--a{left:32px}
  .quote--b{left:236px}
  .quote p{font-size:13px;font-weight:600;line-height:1.1}
  .quote cite{display:block;font-style:normal;font-size:10.5px;font-weight:500;margin-top:12px}
  .quote .mark{position:absolute;font-size:34px;font-weight:800;color:var(--sky);line-height:1}
  .quote .mark--open{left:8px;top:4px}
  .quote .mark--close{right:30px;top:58px}
  .quote--b .mark--close{top:75px;right:18px}
  .guarantee{position:absolute;left:15px;top:225px;width:425px;height:207px;background:var(--peach);color:var(--ink);padding:18px 22px}
  .guarantee h3{font-size:17px;font-weight:600;margin-bottom:8px}
  .guarantee ol{list-style:none}
  .guarantee li{font-size:10.5px;font-weight:500;height:17.8px;display:flex}
  .guarantee li span{width:21px;font-size:8.5px;font-weight:700;padding-top:1px}
  .cta{position:absolute;left:15px;top:432px;width:425px;height:190px;background:var(--white)}
  .cta__fan{position:absolute;left:0;top:8px;width:118px;height:80px;background:radial-gradient(ellipse at center,#8a7a62 0%,#4a3f33 55%,rgba(255,255,255,0) 75%)}
  .bubble{position:absolute;left:105px;top:3px;width:176px;height:88px;background:var(--orange);border:3px solid var(--white);border-radius:50%;box-shadow:0 1px 4px rgba(0,0,0,.3);color:var(--white);text-align:center;font-family:"Roboto Condensed",sans-serif;font-weight:900;transform:rotate(-6deg);padding-top:15px;line-height:1}
  .bubble .a{font-size:26px}
  .bubble .b{font-size:27px;margin-top:2px}
  .cta__hero{position:absolute;left:285px;top:-42px;width:140px;height:160px;background:linear-gradient(160deg,#d9ecff 0%,#6fbf4a 55%,#e4572e 100%);border-radius:14px}
  .brand{position:absolute;left:220px;top:118px;width:190px;display:flex;align-items:center;gap:6px;color:var(--orange);font-weight:800;font-size:19px;text-transform:uppercase;line-height:1}
  .brand__dot{width:12px;height:12px;border-radius:50%;background:var(--orange);flex:none}
  .licence{position:absolute;right:14px;top:172px;font-size:8px;font-weight:600;color:var(--ink)}
  .terms{position:absolute;left:16px;top:128px;width:200px;font-size:6px;font-weight:600;color:var(--ink);line-height:1.3}
  .cards{position:absolute;left:15px;top:150px;display:flex;gap:6px}
  .cards span{width:50px;height:32px;border:1px solid #cfcfcf;border-radius:3px}
  .cards .c1{background:#eb6b1e}
  .cards .c2{background:#1a3d8f}
  .cards .c3{background:#2e8bcf;width:33px}
  .web{position:absolute;right:0;bottom:0;width:217px;height:32px;background:var(--orange);clip-path:polygon(14px 0,100% 0,100% 100%,0 100%);color:var(--white);font-size:12.5px;font-weight:600;display:flex;align-items:center;justify-content:center;padding-left:10px}
</style>
</head>
<body>
<div class="canvas">

  <section class="front">
    <header class="front__head">
      <div class="l1">Hot Sweaty</div>
      <div class="l2">Uncomfortable</div>
    </header>
    <div class="front__photo" role="img" aria-label="Photo of an electrician installing a ceiling fan"></div>
    <footer class="front__foot">
      <div class="save">Save</div>
      <div class="off">Off</div>
      <div class="every">Every 2<sup>nd</sup> Fan Installed</div>
    </footer>
    <div class="price-badge">$25</div>
  </section>

  <section class="back">
    <div class="back__inner"></div>

    <div class="promo">
      <h2>A BREEZE WITHOUT THE COST!</h2>
      <p>Enjoy the gentle breeze &amp; cooling effect of a ceilingfan to help<br>you sleep soundly at night &amp; be moreproductive during the day.</p>
    </div>

    <blockquote class="quote quote--a">
      <span class="mark mark--open">&ldquo;</span>
      <p>We can now sleep!<br>Wow what a difference!<br>Thanks Daniel<br>for your help.</p>
      <span class="mark mark--close">&rdquo;</span>
      <cite>Graham &amp;<br>Lucy Whitford</cite>
    </blockquote>
    <blockquote class="quote quote--b">
      <span class="mark mark--open">&ldquo;</span>
      <p>Super service!<br>What apleasant change.<br>Daniel could not<br>havedone more to ensure<br>our satisfaction..</p>
      <span class="mark mark--close">&rdquo;</span>
      <cite>Tom &amp; Elena - Ryde</cite>
    </blockquote>

    <div class="guarantee">
      <h3>WE GUARANTEE TO</h3>
      <ol>
        <li><span>01.</span>Always be on time, or we pay you $100</li>
        <li><span>02.</span>Tell you the exact cost before any job begins</li>
        <li><span>03.</span>Provide you with a fixed price guarantee, assuring you have no extra costs</li>
        <li><span>04.</span>Leave your place as clean as it was when we first arrived</li>
        <li><span>05.</span>Return, and fix it for free, if its not right</li>
        <li><span>06.</span>Return your telephone calls promptly</li>
        <li><span>07.</span>Provide a minimum 12 Month warranty on all parts</li>
        <li><span>08.</span>Provide friendly, helpful service and advice</li>
      </ol>
    </div>

    <div class="cta">
      <div class="cta__fan" role="img" aria-label="Product photo of a ceiling fan"></div>
      <div class="bubble"><div class="a">CALL NOW !</div><div class="b">1300 482 716</div></div>
      <div class="cta__hero" role="img" aria-label="Illustrated superhero electrician mascot holding a light bulb"></div>
      <div class="terms">Conditions: Mention this ad when booking to receive offer.<br>Limit one per household. Cannot be combined with any other offer</div>
      <div class="cards" aria-label="Accepted payment cards">
        <span class="c1"></span><span class="c2"></span><span class="c3"></span>
      </div>
      <div class="brand"><span class="brand__dot"></span>Bright Spark Electrical</div>
      <div class="licence">LIC NO: 415926C</div>
    </div>

    <div class="web">www.brightsparkelectrical.com.au</div>
  </section>

</div>
</body>
</html>
```